Business Card Design Project: Classically Trained Singer and Voice Teacher

I am a classically trained singer that performs in Opera and Musical Theater and also teaches private voice lessons in those fields. I am looking for a business card that I can give to casting directors and colleagues, as well as to people who are interested in taking voice lessons from me.

This is sort of like an actors business card so I want my headshot and name to be the main focus.

I was kind of thinking of having the business card be horizontal with my headshot photo on the front taking up roughly half and my information on the same side, and perhaps my name again on the back or some form of my initials. But I am totally open to other options for layout.I would prefer to have a double sided business card, but once again, its not essential.

I am looking for it to look and feel elegant artistic and professional, without looking feminine.

Because of the colors of my headshot I would imagine that it would be predominantly brown and white, but I am totally open to other approaches.feel totally free to crop my headshot so that it fits better into your overall design and layout.

It is highly likely that I will ask the winner of the design to create a flyer for marketing my voice lessons with a similar look.

If you have any questions or clarifications, please feel free to ask.

Target Market(s)

Opera and Musical theater casting directors, colleagues; potential voice lesson students

Industry/Entity Type

Marketing

Requirements
Must have
• These must feature prominently:
- (My Headshot (attached))
- Marlow Keating (my name)

These dont need to be as prominent:
- Baritone
- Private Voice Teacher
- Opera and Musical Theater

Contact Info:
Phone: (555) 347-2816
Email: marlkeat@inboxly.example

Nice to have
• Double sided

```html
<!DOCTYPE html>
<html lang="en">
<head>
<meta charset="utf-8">
<title>Marlow Keating – Business Card</title>
<link href="https://fonts.googleapis.com/css2?family=Alfa+Slab+One&family=Arvo:wght@400&display=swap" rel="stylesheet">
<style>
  :root {
    --page: #ffffff;
    --panel: #44546d;
    --ink-light: #ffffff;
    --name-fill: #6d5b4b;
    --name-edge: #b9b6ae;
    --photo-warm: #8a6a4c;
    --photo-mid: #b8a99a;
    --photo-cool: #9aa3ad;
    --shadow: rgba(0, 0, 0, 0.18);
  }
  * { box-sizing: border-box; margin: 0; padding: 0; }
  html, body {
    width: 1200px;
    height: 1012px;
    overflow: hidden;
    background: var(--page);
  }
  .canvas {
    position: relative;
    width: 1200px;
    height: 1012px;
  }
  .card-face {
    position: absolute;
    top: 60px;
    width: 520px;
    height: 898px;
    box-shadow: 0 8px 22px var(--shadow);
  }
  .card-front {
    left: 58px;
    background:
      radial-gradient(ellipse 45% 35% at 55% 32%, #d9b9a0 0%, rgba(217,185,160,0) 100%),
      linear-gradient(180deg, var(--photo-cool) 0%, var(--photo-mid) 30%, var(--photo-warm) 60%, #5d4634 100%);
  }
  .card-back {
    left: 629px;
    background: var(--panel);
    color: var(--ink-light);
    font-family: "Arvo", "Rockwell", serif;
    text-align: center;
  }
  .roles {
    position: absolute;
    top: 100px;
    left: 0;
    right: 0;
  }
  .role {
    font-size: 38px;
    line-height: 1;
    margin-bottom: 34px;
  }
  .role-genre {
    line-height: 40px;
  }
  .name-mark {
    position: absolute;
    top: 405px;
    left: 12px;
    width: 496px;
    height: 200px;
    overflow: visible;
  }
  .name-mark text {
    font-family: "Alfa Slab One", "Rockwell Extra Bold", serif;
    fill: var(--name-fill);
    stroke: var(--name-edge);
    stroke-width: 2.5px;
    paint-order: stroke fill;
  }
  .contact {
    position: absolute;
    top: 762px;
    left: 0;
    right: 0;
  }
  .contact-phone {
    font-size: 50px;
    line-height: 1.1;
  }
  .contact-email {
    font-size: 31px;
    line-height: 1.3;
  }
</style>
</head>
<body>
<main class="canvas">
  <section class="card-face card-front" role="img" aria-label="Headshot of the singer in a brown jacket and striped shirt"></section>

  <section class="card-face card-back">
    <div class="roles">
      <p class="role">Baritone</p>
      <p class="role">Private Voice Teacher</p>
      <p class="role role-genre">Opera &amp; Musical<br>Theater</p>
    </div>

    <svg class="name-mark" viewBox="0 0 496 200" aria-label="Marlow Keating">
      <text x="248" y="70" font-size="76" text-anchor="middle" textLength="490" lengthAdjust="spacingAndGlyphs">MARLOW</text>
      <text x="248" y="178" font-size="112" text-anchor="middle" textLength="490" lengthAdjust="spacingAndGlyphs">KEATING</text>
    </svg>

    <div class="contact">
      <p class="contact-phone">(555) 347-2816</p>
      <p class="contact-email">marlkeat@inboxly.example</p>
    </div>
  </section>
</main>
</body>
</html>
```